FotoVELTA buisnesscard

Hey :) I need a modern buisnesscard for my company FotoVELTA
It most have:
Dagligleder og Fotograf: Henrik Torvald Bjelland

Mob: +4791642058
Epost: post@fotovelta.no
Adresse: Bakkestien22, 4870 Fjordvik

Facbook and instagram logo with text FotoVELTA

FotoVELTA logo

It Company

```html
<!DOCTYPE html>
<html lang="no">
<head>
<meta charset="utf-8">
<title>FotoVELTA business card</title>
<link rel="stylesheet" href="https://fonts.googleapis.com/css2?family=Roboto:wght@400;700&family=Roboto+Condensed:wght@700&family=Saira+Semi+Condensed:wght@700&display=swap">
<style>
  :root {
    --backdrop: #e4e4e4;
    --card-dark: #0a0a0b;
    --card-light: #f7f7f7;
    --brand-blue: #0f73b8;
    --brand-pink: #d2106f;
    --text-grey: #3c3c3c;
    --icon-blue: #1f6fae;
  }
  * { box-sizing: border-box; margin: 0; padding: 0; }
  html, body { width: 1200px; height: 576px; overflow: hidden; background: var(--backdrop); }
  .canvas { position: relative; width: 1200px; height: 576px; font-family: "Roboto", Arial, sans-serif; }

  .card { position: absolute; top: 138px; height: 294px; box-shadow: 0 3px 6px rgba(0,0,0,.25); }

  .card-front { left: 81px; width: 485px; background: var(--card-dark); }
  .front-mark {
    position: absolute; left: 50%; top: 94px; width: 72px; height: 72px;
    transform: translateX(-50%); background: var(--brand-pink);
  }
  .front-name {
    position: absolute; left: 0; right: 0; top: 168px; text-align: center;
    font-weight: 700; font-size: 36px; line-height: 42px; letter-spacing: 1px; color: var(--brand-blue);
  }

  .card-back { left: 602px; width: 482px; background: var(--card-light); overflow: hidden; }
  .side-band { position: absolute; left: 0; top: 0; bottom: 0; width: 42px; background: var(--brand-blue); }
  .side-stripe { position: absolute; left: 42px; top: 0; bottom: 0; width: 4px; background: var(--brand-pink); }

  .back-logo { position: absolute; top: 26px; left: 166px; display: flex; align-items: center; height: 56px; }
  .back-mark { width: 50px; height: 50px; background: var(--brand-pink); }
  .logo-divider { width: 1px; height: 56px; background: #9a9a9a; margin: 0 14px; }
  .back-name { font-weight: 700; font-size: 32px; letter-spacing: .8px; color: var(--brand-blue); }

  .person { position: absolute; left: 64px; top: 160px; }
  .person-name {
    font-family: "Saira Semi Condensed", "Roboto Condensed", sans-serif;
    font-weight: 700; font-size: 20px; line-height: 24px; color: var(--brand-blue);
  }
  .person-role { font-size: 11.5px; color: var(--text-grey); margin-top: 2px; }

  .contact-list { position: absolute; top: 212px; list-style: none; }
  .contact-list.primary { left: 66px; }
  .contact-list.social { left: 302px; }
  .contact-list li { display: flex; align-items: center; height: 17px; font-size: 12.5px; color: var(--text-grey); }
  .contact-list svg { width: 11px; height: 11px; margin-right: 11px; flex: none; fill: var(--icon-blue); }
  .social-dot { width: 10px; height: 10px; margin-right: 11px; background: var(--icon-blue); border-radius: 2px; flex: none; }
</style>
</head>
<body>
<main class="canvas">
  <section class="card card-front" aria-label="Card front">
    <div class="front-mark"></div>
    <div class="front-name">FotoVELTA</div>
  </section>

  <section class="card card-back" aria-label="Card back">
    <div class="side-band"></div>
    <div class="side-stripe"></div>

    <div class="back-logo">
      <div class="back-mark"></div>
      <div class="logo-divider"></div>
      <div class="back-name">FotoVELTA</div>
    </div>

    <div class="person">
      <div class="person-name">Henrik Torvald Bjelland</div>
      <div class="person-role">Managing Director &amp; Photographer</div>
    </div>

    <ul class="contact-list primary">
      <li>
        <svg viewBox="0 0 12 12" aria-hidden="true"><rect x="2.5" y="0" width="7" height="12" rx="1.3"/><rect x="3.7" y="1.5" width="4.6" height="7.5" fill="#f7f7f7"/></svg>
        +4791642058
      </li>
      <li>
        <svg viewBox="0 0 12 12" aria-hidden="true"><rect x="0" y="2" width="12" height="8"/><path d="M0.6 2.6 L6 6.8 L11.4 2.6" fill="none" stroke="#f7f7f7" stroke-width="1.1"/></svg>
        post@fotovelta.no
      </li>
      <li>
        <svg viewBox="0 0 12 12" aria-hidden="true"><path d="M6 0 C3 0 1.5 2.2 1.5 4.3 C1.5 7.2 6 12 6 12 C6 12 10.5 7.2 10.5 4.3 C10.5 2.2 9 0 6 0 Z"/><circle cx="6" cy="4.3" r="1.7" fill="#f7f7f7"/></svg>
        Bakkestien22, 4870 Fjordvik
      </li>
    </ul>

    <ul class="contact-list social">
      <li><span class="social-dot"></span>/FotoVELTA</li>
      <li><span class="social-dot"></span>/FotoVELTA</li>
      <li>
        <svg viewBox="0 0 12 12" aria-hidden="true"><circle cx="6" cy="6" r="5.5"/><path d="M0.5 6 H11.5 M6 0.5 C3.5 3 3.5 9 6 11.5 M6 0.5 C8.5 3 8.5 9 6 11.5" fill="none" stroke="#f7f7f7" stroke-width=".8"/></svg>
        www.fotovelta.no
      </li>
    </ul>
  </section>
</main>
</body>
</html>
```